website creation for contract embroidery company

We are a contract embroider located in Chicago, servicing coast to coast.

Looking for about 5 pages of web design. Home, Gallery, About us, Request Quote.

We also need help with the ad copy itself. I recommend to look at other "contract embroidery" websites to get a sense of what others in our industry is posting.

Industry/Entity Type

Embroidery

Coding

Coded - Design and coding required

Number of Pages Required

1 page

Colors
0356a4
fbee3e

```html
<!DOCTYPE html>
<html lang="en">
<head>
<meta charset="utf-8">
<title>Contract Embroidery</title>
<link href="https://fonts.googleapis.com/css2?family=Roboto:wght@400;500&family=Roboto+Condensed:wght@400;500&family=Lobster&display=swap" rel="stylesheet">
<style>
:root{
  --brand:#0356a4;
  --brand-dark:#0d4aa0;
  --ink:#1b1b1b;
  --text:#333;
  --panel:#e4e4e4;
  --footer:#222;
  --white:#fff;
}
*{margin:0;padding:0;box-sizing:border-box}
html,body{width:836px;height:1200px;overflow:hidden;background:var(--white);font-family:'Roboto',sans-serif;color:var(--text)}
h1,h2,h3,h4{font-weight:400}
.page{position:relative;width:836px;height:1200px}
.abs{position:absolute}
.topline{left:0;top:0;width:836px;height:3px;background:var(--brand-dark)}
.wordmark{left:121px;top:34px;font-family:'Roboto',sans-serif;font-size:20px;font-weight:500;color:var(--ink);letter-spacing:-.2px}
.nav{left:396px;top:44px;display:flex;gap:22px;font-size:9.5px;color:var(--ink)}
.nav .active{color:var(--brand)}
.hero{left:0;top:84px;width:836px;height:387px;background:linear-gradient(180deg,#8fa9c4 0%,#6f8ba6 30%,#4d6f5a 60%,#3f6a74 80%,#4c6f4c 100%)}
.arrow-circle{width:28px;height:28px;border:2px solid var(--white);border-radius:50%;display:flex;align-items:center;justify-content:center}
.hero-title{left:122px;top:208px;font-family:'Lobster',cursive;font-weight:400;font-size:29px;line-height:35px;color:var(--white);text-shadow:0 1px 3px rgba(0,0,0,.4)}
.hero-sub{left:122px;top:285px;font-size:17px;color:var(--white);text-shadow:0 1px 3px rgba(0,0,0,.4)}
.quote{left:509px;top:149px;width:208px;height:245px;background:var(--panel);border-radius:3px;box-shadow:0 2px 6px rgba(0,0,0,.3)}
.quote-head{left:519px;top:142px;width:187px;height:31px;background:var(--brand);color:var(--white);font-size:12.5px;font-weight:500;text-align:center;line-height:31px;box-shadow:0 2px 3px rgba(0,0,0,.25)}
.field{left:526px;width:174px;height:27px;background:var(--white);border:1px solid #ccc;font-size:8.5px;color:#333;padding:8px 7px}
.send{left:569px;top:348px;width:85px;height:26px;background:linear-gradient(#e23a3f,#b81b22);border:1px solid #8e1419;border-radius:2px;color:var(--white);font-size:10px;font-weight:500;text-align:center;line-height:24px}
.section-title{font-size:13px;font-weight:400;color:var(--brand);font-family:'Roboto Condensed',sans-serif}
.mini-arrow{width:15px;height:15px;border:1.5px solid var(--ink);border-radius:50%;display:flex;align-items:center;justify-content:center}
.service-img{top:527px;width:177px;height:109px}
.service-shadow{top:636px;width:177px;height:14px;background:radial-gradient(ellipse at top,rgba(0,0,0,.18),rgba(0,0,0,0) 70%)}
.service-title{top:653px;font-size:9.5px;color:var(--brand);font-family:'Roboto Condensed',sans-serif;font-weight:400}
.service-text{top:673px;width:178px;font-size:7px;line-height:12px;color:var(--ink);text-align:justify}
.band{left:0;top:740px;width:836px;height:216px;background:linear-gradient(90deg,#1a4ea0,#1f56a8 50%,#1b4f9e)}
.welcome-title{left:120px;top:770px;font-size:14px;font-weight:400;color:var(--white)}
.welcome-text{left:121px;top:793px;width:297px;font-size:8.3px;line-height:14.4px;color:#e6ecf7;text-align:justify}
.read-more{left:121px;top:901px;width:75px;height:29px;background:linear-gradient(#fafafa,#c9ced6);border-radius:3px;font-size:10.5px;color:#333;text-align:center;line-height:29px}
.video-frame{left:445px;top:767px;width:270px;height:165px;background:var(--white)}
.video{left:451px;top:772px;width:258px;height:153px;background:linear-gradient(135deg,#2f3f2a,#6e6f58 40%,#d8d1c3 70%,#ede7dc)}
.video-bar{left:451px;top:906px;width:258px;height:19px;background:rgba(20,20,20,.8)}
.col-title{top:994px;font-size:11px;color:var(--brand);font-family:'Roboto Condensed',sans-serif;font-weight:400}
.col-list{top:1021px;font-size:9px;line-height:19.5px;color:var(--text);list-style:none}
.bottom{left:0;top:1104px;width:836px;height:96px;background:var(--footer)}
.bottom-links{left:71px;top:1137px;font-size:9px;color:#e5e5e5}
.copyright{left:71px;top:1156px;font-size:10.5px;color:#e5e5e5}
.social{top:1141px;width:22px;height:22px;border-radius:2px}
</style>
</head>
<body>
<div class="page">
  <div class="abs topline"></div>
  <div class="abs wordmark">CONTRACT EMBROIDERY</div>
  <nav class="abs nav">
    <span class="active">HOME</span><span>GALLERY</span><span>ABOUT US</span><span>REQUEST QUOTE</span><span>CONTACT US</span>
  </nav>

  <section class="abs hero" role="img" aria-label="Aerial photograph of a city skyline, stadium and lakeside harbour"></section>
  <div class="abs arrow-circle" style="left:48px;top:243px">
    <svg width="14" height="14" viewBox="0 0 14 14"><path d="M9 2l-5 5 5 5" stroke="#fff" stroke-width="2" fill="none"/></svg>
  </div>
  <div class="abs arrow-circle" style="left:758px;top:243px">
    <svg width="14" height="14" viewBox="0 0 14 14"><path d="M5 2l5 5-5 5" stroke="#fff" stroke-width="2" fill="none"/></svg>
  </div>
  <h1 class="abs hero-title">Lorem Ipsum is simply dummy<br>text of the printing</h1>
  <p class="abs hero-sub">Lorem Ipsum is simply dummy text</p>

  <div class="abs quote"></div>
  <div class="abs quote-head">REQUEST QUOTE</div>
  <div class="abs field" style="top:198px">Name</div>
  <div class="abs field" style="top:232px">Email id</div>
  <div class="abs field" style="top:266px">Phone</div>
  <div class="abs field" style="top:301px;height:36px">Massage</div>
  <div class="abs send">SENT</div>

  <h2 class="abs section-title" style="left:120px;top:495px">OUR SERVICES</h2>
  <div class="abs mini-arrow" style="left:684px;top:495px"><svg width="7" height="8" viewBox="0 0 7 8"><path d="M5 1l-3 3 3 3" stroke="#1b1b1b" stroke-width="1.3" fill="none"/></svg></div>
  <div class="abs mini-arrow" style="left:701px;top:495px"><svg width="7" height="8" viewBox="0 0 7 8"><path d="M2 1l3 3-3 3" stroke="#1b1b1b" stroke-width="1.3" fill="none"/></svg></div>

  <div class="abs service-img" style="left:123px;background:linear-gradient(135deg,#c9c0b4,#b8413f 45%,#6aa08f 75%,#d2ccc2)" role="img" aria-label="Crocheted flowers in red, pink and green"></div>
  <div class="abs service-img" style="left:328px;background:linear-gradient(135deg,#a9cadb,#c7dde6 45%,#e4553e 60%,#9fc2d4)" role="img" aria-label="Embroidery machine stitching a colourful butterfly"></div>
  <div class="abs service-img" style="left:534px;background:linear-gradient(135deg,#3a2a3a,#5a4cc0 45%,#7bb53a 70%,#3b2c35)" role="img" aria-label="Close-up of a purple embroidered flower"></div>
  <div class="abs service-shadow" style="left:123px"></div>
  <div class="abs service-shadow" style="left:328px"></div>
  <div class="abs service-shadow" style="left:534px"></div>

  <h3 class="abs service-title" style="left:120px">EMBROIDERY</h3>
  <h3 class="abs service-title" style="left:327px">EMBROIDERY</h3>
  <h3 class="abs service-title" style="left:531px">EMBROIDERY</h3>
  <p class="abs service-text" style="left:120px">Lorem Ipsum has been the industry's standard dummy text ever since the 1500s, when an unknown printer took a book. It has survived not only five centuries</p>
  <p class="abs service-text" style="left:327px">Lorem Ipsum has been the industry's standard dummy text ever since the 1500s, when an unknown printer took a book. It has survived not only five centuries</p>
  <p class="abs service-text" style="left:531px">Lorem Ipsum has been the industry's standard dummy text ever since the 1500s, when an unknown printer took a book. It has survived not only five centuries</p>

  <section class="abs band"></section>
  <h2 class="abs welcome-title">WELCOME TO CONTRACT EMBROIDERY</h2>
  <p class="abs welcome-text">Lorem Ipsum is simply dummy text of the printing and typesetting industry. Lorem Ipsum has been the industry's standard dummy text ever since the 1500s, when an unknown printer took a galley of type and scrambled it to make a type specimen book. It has survived not only five centuries, but also the leap into electronic typesetting, remaining essentially unchanged. It was Lorem Ipsum passages, and more recently with desktop publishing software like desktop layout tools including versions of Lorem Ipsum.</p>
  <div class="abs read-more">Read More</div>

  <div class="abs video-frame"></div>
  <div class="abs video" role="img" aria-label="Video still of hands cross-stitching on fabric"></div>
  <svg class="abs" style="left:565px;top:818px" width="32" height="32" viewBox="0 0 32 32"><circle cx="16" cy="16" r="15" fill="rgba(40,40,40,.75)"/><path d="M12 9l11 7-11 7z" fill="#fff"/></svg>
  <div class="abs video-bar"></div>
  <svg class="abs" style="left:451px;top:906px" width="258" height="19" viewBox="0 0 258 19">
    <circle cx="13" cy="9.5" r="4" stroke="#fff" stroke-width="1.2" fill="none"/>
    <path d="M28 7.5h2l3-2v8l-3-2h-2z" fill="#d33"/>
    <rect x="38" y="6" width="14" height="7" fill="#d33" opacity=".8"/>
    <rect x="65" y="8.5" width="112" height="2" fill="#666"/>
    <rect x="65" y="8.5" width="40" height="2" fill="#d2232a"/>
    <text x="186" y="12" font-size="6" fill="#ddd" font-family="Roboto,sans-serif">01:30 / 04:55</text>
    <rect x="227" y="6" width="8" height="6" stroke="#fff" fill="none"/>
    <circle cx="246" cy="9.5" r="3" stroke="#fff" stroke-width="1.5" fill="none"/>
  </svg>

  <h4 class="abs col-title" style="left:120px">COMPANY</h4>
  <ul class="abs col-list" style="left:120px"><li>About us</li><li>Services</li><li>Presentation</li></ul>
  <h4 class="abs col-title" style="left:226px">SPECIALISTS</h4>
  <ul class="abs col-list" style="left:226px"><li>Commercial</li><li>Residential</li><li>Luxury</li></ul>
  <h4 class="abs col-title" style="left:339px">ADVICE</h4>
  <ul class="abs col-list" style="left:339px"><li>FAQs</li><li>Support</li></ul>
  <h4 class="abs col-title" style="left:444px">AGENCIES</h4>
  <ul class="abs col-list" style="left:444px"><li>Sign Up</li><li>Forums</li><li>Promotions</li></ul>
  <h4 class="abs col-title" style="left:545px">CONTACT US</h4>
  <ul class="abs col-list" style="left:545px"><li>1420 Larkspur Avenue, Chicago, IL 60607</li><li>Phone: +1 800 555 0142</li><li>E-mail: hello@stitchline-demo.com</li></ul>

  <footer class="abs bottom"></footer>
  <div class="abs bottom-links">About &nbsp;|&nbsp; Disclaimer &nbsp;|&nbsp; Contact &nbsp;|&nbsp; Sitemap &nbsp;|&nbsp; Hosted Solutions Partner</div>
  <div class="abs copyright">Copyright © 2015 &nbsp;All Rights</div>
  <div class="abs social" style="left:655px;background:#2aa3e0"></div>
  <div class="abs social" style="left:685px;background:#d0201c"></div>
  <div class="abs social" style="left:714px;background:#2f5596"></div>
  <div class="abs social" style="left:744px;background:#1878b5"></div>
</div>
</body>
</html>
```